Chatterly & Instagram Design for: A Lantern for Pim - Notes of a Calm Hound

Need a Chatterly Page and Instagram Page too for helping launch a book as a brand new author with a book on my old dog Pim and the Zen lessons he taught me.
Its all for folks who love dogs and especially rescue dog stories
Its all for folks who are interested in something slightly spiritual and for self growth
I attach the review copy from my publishers who are standing up a website but recommend a Chatterly Page that is attached to my own personal one and an Instagram Page
I intend on publishing weekly "Pimsayings" (The dog was called Pim)
I intend on posting Zen talks (in lay man's terms)
I have a second book being written to follow on the one
Myself as an Author needs profiling
The book needs ALOT of promotion - and we can't travel!
I need to host a bunch of "book talks/launches"
Need to send folks to my website to by the book: Hard/Paperback/Kindle - which comes with book trailer
I have hundreds of photos to give
I have alot of sketches of the dog to share which did not make it into the book
My competition are books like:
Tobin & Us
A Cat Naps Beside Old Farmers
Talo
Duke Ferran's Setter
Lost Shepherd Road
Need this ASAP - publishing date is moved up to October 2021!
Link t Author hot Drop Box: https://www.fileharbor-vault.net/s/kq7wm2201935t4/XXRtplmNvQwerty3ab_KLop?v=0
Link to Dog Photos:
https://www.fileharbor-vault.net/s/pl3rt88vnaw02k/ZZT4k7mnop_Yrw2QLxwbcd9v?v=0
Updates
Hello, I will be in hospitaal having surgery on my neck and request tow more days to =make any kind of small changes. Thank you Harriet
Target Market(s)
Dog owners around the world, especially those wth rescue dogs and those looking for personal growth and those interested in Zen Buddhism
Industry/Entity Type
Author promoting soon to be published book/s
Requirements
Must have
- Author Photo/E-Mail Sign Up/Link to Instagram (see brief to design this)/Link to upcoming website/Link to Author Central (might need to design me something)/Photo Gallery
Nice to have
- Author features and Dog Images (I have new dogs we can show)
Should not have
- Cute - its a meaningful book

```html
<!DOCTYPE html>
<html lang="en">
<head>
<meta charset="utf-8">
<title>A Lantern for Pim – Social Cover Presentation</title>
<link href="https://fonts.googleapis.com/css2?family=Montserrat:wght@500;600;700;800;900&family=Great+Vibes&family=Parisienne&family=Arimo:wght@400;700&display=swap" rel="stylesheet">
<style>
:root{
  --sheet:#eceef2;
  --brand-blue:#1a8bd0;
  --navy:#1f3f8f;
  --ink:#1d2548;
  --violet:#5b4cc4;
  --lilac:#a08ed6;
  --periwinkle:#6e64d2;
  --bar:#3f5ea8;
  --ui-text:#1c1e21;
  --ui-muted:#606770;
  --ui-line:#dddfe2;
  --ui-card:#ffffff;
  --ui-page:#e9ebee;
  --ui-blue:#4267b2;
  --ui-green:#42b72a;
}
*{box-sizing:border-box;margin:0;padding:0}
html,body{width:1200px;height:1200px;overflow:hidden;background:var(--sheet)}
body{position:relative;font-family:'Arimo',Arial,sans-serif;color:var(--ui-text)}

.side-label{position:absolute;font-family:'Montserrat',sans-serif;font-weight:500;color:var(--navy);
  white-space:nowrap;transform:rotate(-90deg);transform-origin:left top}
.side-label--cover{left:40px;top:366px;font-size:34px;letter-spacing:1px}
.side-label--preview{left:1130px;top:1148px;font-size:36px}

/* ---------- cover artwork ---------- */
.cover{position:absolute;width:1032px;height:382px;overflow:hidden;
  background:linear-gradient(180deg,#c9d6e2 0%,#e6edf3 40%,#f4f6f8 62%,#dfe6ee 100%);
  box-shadow:0 2px 6px rgba(0,0,0,.25)}
.cover--main{left:103px;top:20px}
.cover-frame{position:absolute;left:237px;top:464px;width:859px;height:324px;overflow:hidden}
.cover--page{left:0;top:0;transform:scale(.8324);transform-origin:left top;box-shadow:none}

.cover__photo{position:absolute;left:0;top:0;width:500px;height:382px;
  background:
   radial-gradient(ellipse 130px 150px at 190px 110px,#e9c9b3 0%,rgba(233,201,179,0) 100%),
   radial-gradient(ellipse 110px 150px at 360px 260px,#8a6238 0%,rgba(138,98,56,0) 100%),
   radial-gradient(ellipse 210px 180px at 150px 330px,#a81c4c 0%,rgba(168,28,76,0) 100%),
   linear-gradient(90deg,rgba(201,214,226,0) 80%,rgba(226,233,240,1) 100%)}
.cover__ring{position:absolute;left:90px;top:12px;width:420px;height:420px;border-radius:50%;
  border:22px solid rgba(104,76,200,.75);border-left-color:rgba(104,76,200,.15);border-bottom-color:rgba(104,76,200,.35)}

.cover__coming{position:absolute;left:50px;top:244px;font-family:'Montserrat',sans-serif;font-weight:500;
  font-size:46px;color:#fff;text-shadow:0 1px 4px rgba(0,0,0,.35)}
.cover__soon{position:absolute;left:228px;top:206px;font-family:'Great Vibes',cursive;font-size:108px;
  color:#fff;text-shadow:0 1px 4px rgba(0,0,0,.35);line-height:1}

.cover__title{position:absolute;right:26px;top:22px;display:flex;align-items:flex-end;gap:14px;
  font-family:'Montserrat',sans-serif;font-weight:900;color:var(--brand-blue);white-space:nowrap}
.cover__title-lead{font-size:34px;line-height:1;padding-bottom:10px;letter-spacing:.5px}
.cover__title-name{font-size:104px;line-height:.82;letter-spacing:-2px}
.cover__subtitle{position:absolute;left:560px;top:126px;font-family:'Parisienne',cursive;font-size:42px;color:var(--ink);white-space:nowrap}
.cover__author{position:absolute;left:500px;top:209px;font-family:'Montserrat',sans-serif;font-weight:700;font-size:18px;color:var(--ink)}
.cover__date{position:absolute;left:747px;top:202px;width:234px;height:32px;border-radius:16px;background:var(--brand-blue);
  color:#fff;font-family:'Montserrat',sans-serif;font-weight:800;font-size:25px;letter-spacing:1px;text-align:center;line-height:32px}
.cover__quotes{position:absolute;left:490px;width:530px;text-align:center;font-family:'Montserrat',sans-serif;font-weight:600;font-size:25px;white-space:nowrap}
.cover__quotes--one{top:242px;color:var(--lilac)}
.cover__quotes--two{top:274px;color:var(--periwinkle)}
.cover__quotes--two .soft{color:#8e84c8;font-size:21px}
.cover__band{position:absolute;left:469px;top:310px;width:563px;height:42px;background:var(--violet);
  color:#fff;font-family:'Montserrat',sans-serif;font-weight:600;font-size:23px;display:flex;align-items:center;justify-content:center;gap:8px}

/* ---------- page mock ---------- */
.topbar{position:absolute;left:0;top:418px;width:1200px;height:44px;background:var(--bar);border-bottom:1px solid #29487d}
.topbar__name{position:absolute;left:36px;top:11px;font-family:'Montserrat',sans-serif;font-weight:700;font-size:15px;color:#fff}
.topbar__search{position:absolute;left:124px;top:9px;width:412px;height:26px;background:#fff;border-radius:2px}
.topbar__search svg{position:absolute;right:8px;top:5px}
.topbar__nav{position:absolute;right:40px;top:0;height:44px;display:flex;align-items:center;gap:18px;color:#fff;font-weight:700;font-size:13px}
.topbar__sep{width:1px;height:20px;background:rgba(255,255,255,.3)}

.profile{position:absolute;left:38px;top:476px;width:188px;height:188px;border-radius:50%;background:#fff;
  border:3px solid #f3f4f6;box-shadow:0 0 0 1px #dfe1e5;display:flex;flex-direction:column;align-items:center;justify-content:center}
.profile__art{width:110px;height:70px;border-radius:40px;background:radial-gradient(ellipse at center,#bfc3c9,#eef0f2)}
.profile__name{margin-top:6px;font-family:'Montserrat',sans-serif;font-weight:800;font-size:17px;color:var(--navy);text-align:center;line-height:1.05}

.sidenav{position:absolute;left:35px;top:802px;width:187px;list-style:none;font-size:14px;color:var(--ui-text)}
.sidenav li{height:32.5px;line-height:30px;padding-left:8px}
.sidenav li.is-active{background:#f5f6f7;border:1px solid var(--ui-line);font-weight:700}
.create-page{position:absolute;left:40px;top:1042px;width:98px;height:24px;background:var(--ui-green);color:#fff;font-weight:700;font-size:12px;border-radius:2px;text-align:center;line-height:24px}

.card{position:absolute;background:var(--ui-card);border:1px solid var(--ui-line)}
.actions{left:237px;top:790px;width:859px;height:53px}
.btn-group{position:absolute;left:13px;top:11px;height:29px;display:flex;border:1px solid #ccd0d5;border-radius:2px;background:#f5f6f7}
.btn-group span{display:flex;align-items:center;gap:5px;padding:0 11px;font-size:12px;font-weight:700;color:#4b4f56;border-right:1px solid #ccd0d5}
.btn-group span:last-child{border-right:0}
.btn-email{position:absolute;left:545px;top:11px;width:148px;height:29px;background:var(--ui-blue);color:#fff;font-size:14px;text-align:center;line-height:29px;border-radius:2px}
.btn-message{position:absolute;left:705px;top:11px;width:141px;height:29px;border:1px solid #ccd0d5;background:#f5f6f7;color:#4b4f56;font-size:14px;display:flex;align-items:center;justify-content:center;gap:6px;border-radius:2px}
.dot-icon{width:15px;height:15px;border-radius:50%;background:#8d949e;display:inline-block}

.composer{left:238px;top:858px;width:523px;height:162px}
.composer__head{position:absolute;left:14px;top:9px;right:14px;padding-bottom:9px;border-bottom:1px solid var(--ui-line);font-size:13px;font-weight:700;color:#4b4f56;padding-left:16px}
.composer__avatar{position:absolute;left:14px;top:52px;width:42px;height:42px;border-radius:50%;border:1px solid var(--ui-line);background:radial-gradient(circle,#dfe3ea,#fff)}
.composer__field{position:absolute;left:67px;top:64px;font-size:14px;color:#90949c}
.composer__emoji{position:absolute;right:8px;top:88px;width:16px;height:16px;border-radius:50%;border:1.5px solid #90949c}
.composer__rule{position:absolute;left:14px;right:14px;top:111px;border-top:1px solid var(--ui-line)}
.composer__tools{position:absolute;left:14px;top:122px;display:flex;gap:9px}
.chip{height:32px;border-radius:16px;background:#f2f3f5;display:flex;align-items:center;gap:6px;padding:0 14px 0 10px;font-size:13px;font-weight:700;color:#4b4f56}

.photos{left:238px;top:1033px;width:523px;height:180px}
.card__title{position:absolute;left:13px;top:11px;font-size:15px;font-weight:700}
.photos .card__rule{position:absolute;left:0;right:0;top:41px;border-top:1px solid var(--ui-line)}

.rating{left:774px;top:858px;width:322px;height:59px}
.rating__icon{position:absolute;left:14px;top:14px;width:30px;height:30px;border-radius:50%;background:#d6d9dd;display:flex;align-items:center;justify-content:center}
.rating__text{position:absolute;left:54px;top:21px;font-size:12px;color:var(--ui-text)}
.community{left:774px;top:931px;width:322px;height:71px}
.see-all{position:absolute;right:13px;top:13px;font-size:12px;color:var(--ui-muted)}
.community__invite{position:absolute;left:13px;top:47px;font-size:12px;color:var(--ui-text);display:flex;gap:10px;align-items:center}
.community__invite b{color:#365899}
.about{left:774px;top:1014px;width:322px;height:200px}
.about__icons{position:absolute;left:13px;top:42px;display:flex;flex-direction:column;gap:13px}
</style>
</head>
<body>

<div class="side-label side-label--cover">COVER CHATTERLY</div>

<section class="cover cover--main" aria-label="Cover banner">
  <div class="cover__photo" role="img" aria-label="Author photo: smiling woman in a magenta coat kneeling beside her brindle dog against a cloudy sky"></div>
  <div class="cover__ring"></div>
  <div class="cover__coming">Coming</div>
  <div class="cover__soon">Soon</div>
  <h1 class="cover__title"><span class="cover__title-lead">A LANTERN FOR</span><span class="cover__title-name">PIM</span></h1>
  <div class="cover__subtitle">Notes of a Calm Hound</div>
  <div class="cover__author">— HARRIET VOSSLUND</div>
  <div class="cover__date">OCTOBER 2021</div>
  <div class="cover__quotes cover__quotes--one">“Thoughtful Insights”</div>
  <div class="cover__quotes cover__quotes--two"><span class="soft">“Zen Wisdom”</span>&nbsp; “Human Lessons on Life”</div>
  <div class="cover__band">Visit
    <svg width="20" height="20" viewBox="0 0 20 20" fill="none" stroke="#fff" stroke-width="1.5"><circle cx="10" cy="10" r="8"/><ellipse cx="10" cy="10" rx="3.5" ry="8"/><path d="M2 10h16M3.5 6h13M3.5 14h13"/></svg>
    pimlantern-site.com</div>
</section>

<header class="topbar">
  <div class="topbar__name">Chatterly</div>
  <div class="topbar__search"><svg width="16" height="16" viewBox="0 0 16 16" fill="none" stroke="#4b4f56" stroke-width="2"><circle cx="6.5" cy="6.5" r="5"/><path d="M10.5 10.5l4 4"/></svg></div>
  <nav class="topbar__nav">
    <span class="topbar__sep"></span><span>Home</span><span class="topbar__sep"></span><span>Create</span><span class="topbar__sep"></span>
    <svg width="22" height="18" viewBox="0 0 22 18" fill="#1d2a4a"><circle cx="8" cy="5" r="4"/><path d="M0 17c0-5 4-7 8-7s8 2 8 7z"/><circle cx="16" cy="5" r="3"/><path d="M14 10c4 0 8 2 8 7h-5c0-3-1-5-3-7z"/></svg>
    <span class="dot-icon" style="background:#1d2a4a;width:20px;height:20px"></span>
    <svg width="20" height="20" viewBox="0 0 20 20" fill="#1d2a4a"><path d="M10 1c-4 0-6 3-6 7v4l-2 3h16l-2-3V8c0-4-2-7-6-7z"/><circle cx="10" cy="17.5" r="2"/></svg>
    <span class="topbar__sep"></span>
    <svg width="22" height="22" viewBox="0 0 22 22"><circle cx="11" cy="11" r="10" fill="#1d2a4a"/><text x="11" y="16" text-anchor="middle" font-size="14" font-weight="700" fill="#3f5ea8" font-family="Arial">?</text></svg>
    <svg width="12" height="8" viewBox="0 0 12 8" fill="#1d2a4a"><path d="M0 0h12L6 7z"/></svg>
  </nav>
</header>

<div class="profile">
  <div class="profile__art" role="img" aria-label="Pencil sketch of the dog Pim"></div>
  <div class="profile__name">A LANTERN<br>FOR PIM</div>
</div>

<ul class="sidenav">
  <li class="is-active">Home</li><li>Services</li><li>Reviews</li><li>Photos</li><li>Posts</li><li>About</li><li>Community</li>
</ul>
<div class="create-page">Create a Page</div>

<div class="cover-frame">
  <section class="cover cover--page" aria-label="Cover banner in page preview">
    <div class="cover__photo" role="img" aria-label="Author photo: smiling woman in a magenta coat kneeling beside her brindle dog against a cloudy sky"></div>
    <div class="cover__ring"></div>
    <div class="cover__coming">Coming</div>
    <div class="cover__soon">Soon</div>
    <div class="cover__title"><span class="cover__title-lead">A LANTERN FOR</span><span class="cover__title-name">PIM</span></div>
    <div class="cover__subtitle">Notes of a Calm Hound</div>
    <div class="cover__author">— HARRIET VOSSLUND</div>
    <div class="cover__date">OCTOBER 2021</div>
    <div class="cover__quotes cover__quotes--one">“Thoughtful Insights”</div>
    <div class="cover__quotes cover__quotes--two"><span class="soft">“Zen Wisdom”</span>&nbsp; “Human Lessons on Life”</div>
    <div class="cover__band">Visit
      <svg width="20" height="20" viewBox="0 0 20 20" fill="none" stroke="#fff" stroke-width="1.5"><circle cx="10" cy="10" r="8"/><ellipse cx="10" cy="10" rx="3.5" ry="8"/><path d="M2 10h16M3.5 6h13M3.5 14h13"/></svg>
      pimlantern-site.com</div>
  </section>
</div>

<div class="card actions">
  <div class="btn-group">
    <span><svg width="12" height="12" viewBox="0 0 12 12" fill="#4b4f56"><path d="M0 5h3v7H0zM4 5l3-5c1 0 2 1 1.5 2.5L8 4h3.5c.5 0 .8.6.6 1L10.5 11c-.2.6-.6 1-1.2 1H4z"/></svg>Like</span>
    <span><svg width="12" height="12" viewBox="0 0 12 12" fill="none" stroke="#4b4f56" stroke-width="1.5"><path d="M1 1a10 10 0 0 1 10 10M1 5a6 6 0 0 1 6 6"/><circle cx="2" cy="10" r="1.3" fill="#4b4f56"/></svg>Follow</span>
    <span><svg width="13" height="11" viewBox="0 0 13 11" fill="#4b4f56"><path d="M7 0l6 5-6 5V7C3 7 1 8 0 11 0 6 3 3 7 3z"/></svg>Share</span>
    <span>•••</span>
  </div>
  <div class="btn-email">Send Email</div>
  <div class="btn-message"><span class="dot-icon"></span>Send Message</div>
</div>

<div class="card composer">
  <div class="composer__head">Create Post</div>
  <div class="composer__avatar" role="img" aria-label="Page profile sketch"></div>
  <div class="composer__field">Write a post...</div>
  <div class="composer__emoji"></div>
  <div class="composer__rule"></div>
  <div class="composer__tools">
    <span class="chip"><svg width="18" height="16" viewBox="0 0 18 16"><rect x="1" y="1" width="16" height="14" rx="2" fill="#8ed0f0" stroke="#3b8ccc"/><path d="M2 14l5-6 4 4 2-2 4 4z" fill="#5cb85c"/></svg>Photo/Video</span>
    <span class="chip"><svg width="18" height="16" viewBox="0 0 18 16" fill="#4a90e2"><circle cx="8" cy="5" r="4"/><path d="M0 16c0-5 4-7 8-7s8 2 8 7z"/></svg>Tag Friends</span>
    <span class="chip"><svg width="14" height="18" viewBox="0 0 14 18"><path d="M7 0a7 7 0 0 1 7 7c0 5-7 11-7 11S0 12 0 7a7 7 0 0 1 7-7z" fill="#f0284a"/><circle cx="7" cy="7" r="2.5" fill="#fff"/></svg>Check in</span>
    <span class="chip" style="padding:0 14px">•••</span>
  </div>
</div>

<div class="card photos"><div class="card__title">Photos</div><div class="card__rule"></div></div>

<div class="card rating">
  <div class="rating__icon"><svg width="14" height="14" viewBox="0 0 14 14" fill="#fff"><path d="M7 1l1.8 3.8 4.2.5-3.1 2.9.8 4.1L7 10.3 3.3 12.3l.8-4.1L1 5.3l4.2-.5z"/></svg></div>
  <div class="rating__text">No Rating Yet</div>
</div>

<div class="card community">
  <div class="card__title">Community</div><div class="see-all">See All</div>
  <div class="community__invite"><svg width="18" height="14" viewBox="0 0 22 18" fill="#8d949e"><circle cx="8" cy="5" r="4"/><path d="M0 17c0-5 4-7 8-7s8 2 8 7z"/><circle cx="16" cy="5" r="3"/></svg><span><b>Invite your friends</b> to like this Page</span></div>
</div>

<div class="card about">
  <div class="card__title">About</div><div class="see-all">See All</div>
  <div class="about__icons">
    <svg width="20" height="20" viewBox="0 0 20 20" fill="none" stroke="#606770" stroke-width="1.3"><path d="M4 2l3 1 1 4-2 1c1 3 3 5 6 6l1-2 4 1 1 3-2 2C9 18 2 11 2 4z"/></svg>
    <svg width="20" height="20" viewBox="0 0 20 20" fill="none" stroke="#606770" stroke-width="1.3"><circle cx="10" cy="10" r="8"/></svg>
    <svg width="20" height="20" viewBox="0 0 20 20" fill="none" stroke="#606770" stroke-width="1.3"><circle cx="10" cy="10" r="8"/><ellipse cx="10" cy="10" rx="3.5" ry="8"/><path d="M2 10h16"/></svg>
    <svg width="20" height="20" viewBox="0 0 20 20" fill="none" stroke="#606770" stroke-width="1.3"><rect x="2" y="4" width="16" height="13"/><path d="M2 8h16"/></svg>
    <svg width="20" height="20" viewBox="0 0 20 20" fill="none" stroke="#606770" stroke-width="1.3"><path d="M3 17l1-4 10-10 3 3-10 10z"/></svg>
  </div>
</div>

<div class="side-label side-label--preview">look and feel after adding in chatterly</div>

</body>
</html>
```